Creative Brief
business card QV HAIR CARE
QV HAIR CARE
Bright & Fun-filled
DORIAN FELKOSTA
PO Box 5817 WILLOWMERE
CA 90478
df@qvhaircare-example.com
qvhaircare-example.com
current logo
tire tracks

```html
<!DOCTYPE html>
<html lang="en">
<head>
<meta charset="utf-8">
<title>QV Hair Care – Business Card</title>
<link rel="stylesheet" href="https://fonts.googleapis.com/css2?family=Oxanium:wght@500;700&display=swap">
<style>
  :root {
    --stage: #2b2b2b;
    --card-black: #0b0b0b;
    --card-white: #ffffff;
    --lime: #9fd41c;
    --lime-deep: #5f9a12;
    --grey-text: #cfcfcf;
    --rule: #3a3a3a;
  }
  * { box-sizing: border-box; margin: 0; padding: 0; }
  html, body { width: 1200px; height: 643px; overflow: hidden; }
  body {
    background: var(--stage);
    font-family: "Oxanium", sans-serif;
    position: relative;
  }
  .card {
    position: absolute;
    top: 190px;
    width: 470px;
    height: 268px;
    background: var(--card-black);
    overflow: hidden;
    box-shadow: 0 6px 18px rgba(0,0,0,.45);
  }
  .card--front { left: 80px; }
  .card--back { left: 650px; }

  .front-curve { position: absolute; inset: 0; }

  .brand-name {
    position: absolute;
    font-weight: 700;
    color: var(--lime-deep);
    letter-spacing: 1px;
    white-space: nowrap;
  }
  .card--front .brand-name { left: 28px; top: 112px; font-size: 28px; }

  .contact-name {
    position: absolute;
    right: 26px; top: 22px;
    font-size: 13px;
    font-weight: 700;
    letter-spacing: 1.5px;
    color: var(--lime);
  }
  .contact-rule {
    position: absolute;
    left: 250px; right: 22px; top: 44px;
    height: 1px;
    background: var(--rule);
  }
  .contact-list {
    position: absolute;
    left: 268px; top: 56px;
    list-style: none;
    font-size: 9px;
    font-weight: 500;
    color: var(--grey-text);
    line-height: 14px;
  }
  .contact-list li { display: flex; align-items: flex-start; gap: 6px; }
  .contact-list svg { flex: none; margin-top: 3px; }
  .contact-list .phone { margin-top: 10px; }

  .product-photo {
    position: absolute;
    left: 238px; top: 120px;
    width: 186px; height: 110px;
    background: linear-gradient(90deg, #b0121a 0%, #3a3f56 35%, #2f5c6e 60%, #c0131c 100%);
    border-radius: 4px;
  }
  .card--front .web-email {
    position: absolute;
    left: 28px; bottom: 26px;
    font-size: 12px;
    font-weight: 500;
    color: var(--lime);
  }

  .track-texture {
    position: absolute;
    left: 0; right: 0; top: 30px; height: 150px;
    background: linear-gradient(180deg, #1a1a1a 0%, #7a7a7a 40%, #6b8f22 70%, #1a1a1a 100%);
    opacity: .8;
  }
  .card--back .brand-name {
    left: 0; right: 0; top: 100px;
    text-align: center;
    font-size: 38px;
    color: var(--lime);
  }
  .card--back .web-address {
    position: absolute;
    left: 0; right: 0; bottom: 34px;
    text-align: center;
    font-size: 13px;
    font-weight: 500;
    color: var(--lime);
  }
</style>
</head>
<body>
  <section class="card card--front" aria-label="Business card front">
    <svg class="front-curve" width="470" height="268" viewBox="0 0 470 268" aria-hidden="true">
      <path d="M0 0 H215 C250 60 230 150 150 195 C100 222 50 228 0 230 Z" fill="var(--card-white)"/>
    </svg>
    <div class="brand-name">QV HAIR CARE</div>
    <p class="contact-name">DORIAN FELKOSTA</p>
    <div class="contact-rule"></div>
    <ul class="contact-list">
      <li>
        <svg width="7" height="9" viewBox="0 0 7 9" aria-hidden="true"><path d="M3.5 0a3.5 3.5 0 0 1 3.5 3.5C7 6 3.5 9 3.5 9S0 6 0 3.5A3.5 3.5 0 0 1 3.5 0z" fill="var(--lime)"/></svg>
        <span>PO Box 5817 WILLOWMERE<br>CA 90478</span>
      </li>
      <li class="phone">
        <svg width="7" height="9" viewBox="0 0 7 9" aria-hidden="true"><rect x="0.5" y="0.5" width="6" height="8" rx="1.2" fill="none" stroke="var(--lime)"/></svg>
        <span>818 555 0142</span>
      </li>
    </ul>
    <div class="product-photo" role="img" aria-label="Photo of hair care product bottles and tubs"></div>
    <p class="web-email">df@qvhaircare-example.com</p>
  </section>

  <section class="card card--back" aria-label="Business card back">
    <div class="track-texture" role="img" aria-label="Grey and lime tire track texture"></div>
    <div class="brand-name">QV HAIR CARE</div>
    <p class="web-address">qvhaircare-example.com</p>
  </section>
</body>
</html>
```